Psychologist Banner Ads for Remarketing & yarnwave

Brand awareness campaign for tallowbridge.com.au

// Ad Formats //
Static JPEG
Max 45KB in file size
All ads must have a border

// Ad Sizes //
Static: (for Zindle Display network) 300×250, 160×600, 728×90
Static: (for Yarnwave, no more than 25% text): 600×315, 1200 x 627

Please use logo, image and "maximise your wellbeing" from the website home page.

```html
<!DOCTYPE html>
<html lang="en">
<head>
<meta charset="utf-8">
<title>Tallowbridge Psychology – Maximise Your Wellbeing</title>
<link rel="stylesheet" href="https://fonts.googleapis.com/css2?family=Roboto:wght@300;400;700&display=swap">
<style>
  :root {
    --navy: #0b3a8e;
    --navy-deep: #082f78;
    --sky-text: #cfe5ff;
    --white: #ffffff;
    --frame-line: rgba(200, 220, 245, 0.75);
    --band-light: #3fa2cc;
    --band-mid: #2f90c0;
    --band-edge: #e8f4fb;
    --brand-blue: #1f4f8f;
  }
  html, body {
    margin: 0;
    padding: 0;
    overflow: hidden;
    background: #ffffff;
  }
  .banner {
    position: relative;
    width: 1200px;
    height: 628px;
    overflow: hidden;
    background: linear-gradient(180deg, var(--navy-deep) 0%, var(--navy) 100%);
    font-family: "Roboto", Arial, sans-serif;
  }
  .banner__shapes {
    position: absolute;
    inset: 0;
  }
  .headline {
    position: absolute;
    left: 0;
    top: 0;
    width: 1200px;
    height: 200px;
    margin: 0;
    letter-spacing: -0.04em;
    line-height: 1;
  }
  .headline__main {
    position: absolute;
    left: 238px;
    top: 14px;
    font-size: 108px;
    font-weight: 700;
    color: var(--sky-text);
  }
  .headline__sub {
    position: absolute;
    left: 396px;
    top: 104px;
    font-size: 88px;
    font-weight: 300;
    color: var(--white);
    white-space: nowrap;
  }
  .headline__accent {
    font-weight: 700;
    color: var(--sky-text);
  }
  .brand {
    position: absolute;
    left: 130px;
    top: 285px;
    color: var(--brand-blue);
    font-weight: 400;
    line-height: 1;
  }
  .brand__name {
    display: block;
    font-size: 68px;
    letter-spacing: -0.02em;
  }
  .brand__field {
    display: block;
    margin-top: 34px;
    font-size: 40px;
    letter-spacing: 0.08em;
  }
</style>
</head>
<body>
  <div class="banner">
    <svg class="banner__shapes" width="1200" height="628" viewBox="0 0 1200 628">
      <defs>
        <linearGradient id="ocean-photo" x1="0" y1="0" x2="1" y2="0">
          <stop offset="0" stop-color="#eef4f9"/>
          <stop offset="0.3" stop-color="#c9dbe9"/>
          <stop offset="0.45" stop-color="#6f86b6"/>
          <stop offset="0.58" stop-color="#c99a80"/>
          <stop offset="0.7" stop-color="#f0e2d8"/>
          <stop offset="0.8" stop-color="#3a57a8"/>
          <stop offset="1" stop-color="#243c8c"/>
        </linearGradient>
      </defs>

      <g class="frame" fill="none" stroke="var(--frame-line)" stroke-width="2">
        <path d="M40 205 V72 H232"/>
        <path d="M712 72 H1165 V238"/>
      </g>

      <path class="photo" role="img"
            aria-label="Photo: a joyful woman with arms raised in front of a crashing blue ocean wave"
            fill="url(#ocean-photo)"
            d="M0 220 C250 185 500 175 700 190 C900 205 1050 225 1200 232 V628 H0 Z"/>

      <path class="band band--light" fill="var(--band-light)"
            d="M0 478 H560 C820 478 1020 560 1200 628 H0 Z"/>
      <path class="band band--edge" fill="none" stroke="var(--band-edge)" stroke-width="3"
            d="M0 548 C400 545 860 555 1160 628"/>
      <path class="band band--mid" fill="var(--band-mid)"
            d="M0 550 C400 547 860 557 1158 628 H0 Z"/>
    </svg>

    <h1 class="headline">
      <span class="headline__main">Maximise</span>
      <span class="headline__sub">Your <span class="headline__accent">Well</span>being</span>
    </h1>

    <div class="brand">
      <span class="brand__name">Tallowbridge</span>
      <span class="brand__field">PSYCHOLOGY</span>
    </div>
  </div>
</body>
</html>
```